Web Design with a Twist! Not cheap design

Please note that this project is ending at 5pm on Tuesday the 28th of September, Australian Western Standard Time!!

Please also note that this project has now been guaranteed!

This project involves three primary elements:
* Logo design;
* Web design - of additional pages and page elements to fit into a site that is already in design/development;
* Graphic design - various images used on the site.

The following materials are included for the project:
* Project requirements
* Company / Site name
* Company / Site description
* Wireframes for new pages / page elements
* Screenshots of existing designs and accompanying definition of constraints for new designs
* PSDs for existing site designs
* Technical requirements for designs
* Content (to guide designs)

Project Requirements:

* Logo design:
This is a new company / site, so we need a new logo. We want to see what you come up with here without giving too much direction that may restrict creativity. If desired, you may find possible guidance through considering the company name, company description, and the existing site designs. Please note that the current logo in the site is for placeholder purposes only.

* Web design:
We need the following pages (and features) to be designed for the site:
• Home page
• Advertise page
• How it works page
We’ve provided some wireframes for the pages, however we definitely don't want you to be guided by the layout/styling at all - the wireframes are only there to indicate the features that we require on each page only. So please ignore all aspects of the wireframes except for the indications of features and functionality.

* Graphic design:
We need various images to be designed throughout the site. These include:
• The image at the top of the ‘Home’ page – please note we will provide some direction on this asap
• The image at the top of the ‘Advertise’ page – please note we will provide some direction n this asap
• The image at the top of the ‘How it Works’ pages
• The images that accompany each of the left hand menu items on the ‘How it Works’ pages (the main images & thumbnails if that’s part of your design). Please note that these images need to be constructed to match the Headlines for each of the ‘What’, ‘Who’, ‘Where’, etc menu items. These Headlines (and some descriptive text) can be found in the Content section at the end of this brief.
• The map of Australia for the ‘Home’ page
• The images to accompany the pricing section of the ‘Advertise’ page
• The variations of the ‘Life in the search lane’ images that are used on the ‘Home’, ‘Advertise’, and ‘How it Works’ pages. Please note that if you want to use different imagery (or no imagery, dependent upon your design) for the Home and Advertise pages then this is your call.

Company Name:
TaskBloom

Company / Site description:
This site will provide a means for contractors ('advertisers') to easily specify and advertise their services, coupled with a means for employers (‘buyers’) to easily seek out and contact these people.
The site will cater for contractor-side advertisements only; job postings will not be accommodated (turning the traditional job advertisement model on its head).
In general, the functionality of the site is somewhat like a mashup of sites like crewvault.com and stayvane.com. The site will incorporate the following primary features of contractor profile display and search, company profile display, (and an availability calendar for v2 release).

Constraints for designs:
On some of the existing designs you will notice that a number of the elements of the site have already been designed. When constructing your designs, please work in accordance with the following constraints:

You have to keep:
• Colour scheme in the header
• Colour scheme in the top navigation buttons (including text colour and background colour)
• Colour scheme for the buttons like on the Register page

You can ignore:
• The existing placeholder logo
• Border, layout, and colour scheme for page elements (like the lines around and inside the register section on the Register page)
• Design of text fields
• Font colour scheme throughout the site – the orange and grey headlines and body text
• Design and colour scheme of the map of Australia
• The breadcrumbs (whether or not they appear, and their layout, styling, colour scheme etc)
• Dropdown styling (assuming you had to make some; currently not on any pages we’re asking you to do) like on the Browse Profession page
• Profile styling (for the home page featured profiles) like on the Browse Profession page
• Footer styling
• Anything else we haven’t explicitly asked you to keep

Technical requirements for design:
Any site designs in either Layered Photoshop files (PSD's) or Illustrator Drawings (AI). RGB Color. Must fit current site design, we work to 1024 wide screens. Usuable area is defined in site designs that are attached in the Photoshop documents; it's around 960px.
Logo work needs to be Illustrator Drawings (AI) and EPS. Need CMYK images for printing and RGB for screen. Logos must include any special fonts that are used as TTF or Open Type. Logos need Color, Monochrome, Reversed and both Tall and Wide usages.

Content for the 'How it Works' pages - this content should guide the images that appear on each page.
* What
Headline: TaskBloom brings contractors and employers together
Descriptive text: (turns the traditional job search model on its head)
* Who
Headline: TaskBloom is for highly skilled professionals and fast moving companies
Descriptive text:
* Where
Headline: Anywhere in Australia, TaskBloom is working by your side
Descriptive text:
* Why
Headline: There are more than 1 million reasons to love TaskBloom
Descriptive text: In Australia, there are 1 million people who work as contractors in their main job, and a further 100,000 people who are contractors in their second job. That’s a lot of contractors!
* When
Headline: TaskBloom is forming partnerships 24 hours a day
Descriptive text:
* How
Headline: Life in the search lane, with TaskBloom
Descriptive text: Advertise on TaskBloom now, and get your life in the search lane.

Remember
Just remember the wireframes we have submitted are just a guide – we want to see your creativity shine. And above all else - have fun!
Thank you.
Updates

Please note the deadline for this design competition 5pm on Tuesday the 28th of September, Australian Western Standard Time.

Just under 3 days away!

The deadline of the project will soon be updated to reflect this.

Hi Designers!

Just to be 100% clear about the deadline - the timer is currently showing 7 hours too many. In other words, the project will end 7 hours before the timer finishes.

I will send a notification if the timer starts to display the correct time. So until then, please remember that the deadline is earlier than it seems!

Thanks

Hi Designers,

A couple of really important points:

Firstly - if everyone could please stick to the theme that we provided in the Photoshop files that would be excellent. It is not possible for us to create a new theme. We're dealing with very tight deadlines, so please just provide designs that fit within the current theme.

Secondly, we were really hoping for more illustrations / graphics to be provided in the designs. We're not a fan of the stock photos of generic business people. So please send through designs that incorporate illustrations / graphics for any imagery.

Also just a reminder that this competition is still ending 7 hours earlier than the timer currently displays.

Thanks.

Target Market(s)

The ‘advertiser’ target market for the site is white collar professionals, in all types of industries. The site will be catering for premium contractors only. The site will be catering for both 'in person' contractors, as well as 'knowledge economy' contractors. The site will not be seeking to compete with gigmora.com, plixo.com, taskrune.com, or similar sites.

The advertiser target market will also encompass companies and labour hire agencies that have contractors in their workforce.

The ‘buyer’ target market will encompass employers, recruitment agents, and member-to-member hiring.

Industry/Entity Type

Contractor

Requirements
Must have
• As per overview
Nice to have
• As per overview
Should not have
• As per overview

```html
<!DOCTYPE html>
<html lang="en">
<head>
<meta charset="utf-8">
<title>TaskBloom – Home</title>
<link rel="stylesheet" href="https://fonts.googleapis.com/css2?family=Ubuntu:wght@400;500;700&family=Questrial&family=Noto+Sans:wght@400;700&display=swap">
<style>
  :root {
    --header: #67778b;
    --header-dark: #56667a;
    --tab: #a8b3c1;
    --tab-text: #e9edf2;
    --orange: #f96a2b;
    --orange-dark: #e4561b;
    --peach: #fdd4bc;
    --green: #5cbc3c;
    --ink: #2b2b2b;
    --body: #333;
    --muted: #9aa2ab;
    --line: #e2e2e2;
    --page: #f7f7f7;
  }
  * { box-sizing: border-box; margin: 0; padding: 0; }
  html, body { width: 972px; height: 1200px; overflow: hidden; }
  body { position: relative; background: var(--page); font-family: "Noto Sans", Verdana, sans-serif; color: var(--body); }
  .abs { position: absolute; }

  .site-header { left: 0; top: 0; width: 972px; height: 117px; background: linear-gradient(var(--header), var(--header-dark)); }
  .brand { left: 29px; top: 0; width: 239px; height: 107px; background: linear-gradient(#f9772f, #e85f1c); box-shadow: 0 2px 4px rgba(0,0,0,.3); display: flex; align-items: center; justify-content: center; gap: 10px; }
  .brand-dot { width: 16px; height: 16px; border-radius: 50%; background: #fff; }
  .brand-name { font-family: "Ubuntu", sans-serif; font-weight: 700; font-size: 30px; color: #fff; letter-spacing: 1px; }

  .nav-tab { top: 85px; height: 32px; border-radius: 8px 8px 0 0; background: var(--tab); color: var(--tab-text); font-family: "Ubuntu", sans-serif; font-weight: 500; font-size: 17px; display: flex; align-items: center; justify-content: center; }
  .nav-tab.home { background: #fff; }

  .search { left: 702px; top: 131px; width: 240px; height: 24px; border: 1px solid #8c9bab; border-radius: 3px; background: #fff; display: flex; }
  .search-field { flex: 1; display: flex; align-items: center; gap: 5px; padding-left: 6px; font-family: Arial, sans-serif; font-size: 13px; color: #8a8f96; }
  .search-go { width: 39px; background: #8b99a9; color: #fff; font: 700 13px Arial, sans-serif; display: flex; align-items: center; justify-content: center; }

  .hero { left: 29px; top: 165px; width: 913px; height: 255px; background: #fff; border: 1px solid var(--line); }
  .hero-title { left: 31px; top: 28px; font-family: "Questrial", sans-serif; font-size: 19px; color: var(--ink); }
  .hero-title em, .accent { font-style: normal; color: var(--orange); font-family: "Ubuntu", sans-serif; font-weight: 500; }
  .hero-text { left: 30px; top: 65px; width: 380px; font-size: 12.2px; line-height: 17.5px; color: var(--ink); }
  .btn-orange { left: 30px; top: 205px; width: 110px; height: 27px; background: var(--orange); border-radius: 3px; color: #fff; font: 500 15px "Ubuntu", sans-serif; display: flex; align-items: center; justify-content: center; }
  .dot { top: 224px; width: 9px; height: 9px; border-radius: 50%; background: #c9c9c9; }
  .dot.on { background: var(--orange); }
  .hero-art { left: 436px; top: 10px; width: 463px; height: 230px; border: 4px solid #fff; box-shadow: 0 0 3px rgba(0,0,0,.35); background: linear-gradient(90deg, #f3f3f3, #dcdcdc); }

  .welcome-title { left: 30px; top: 440px; font-family: "Questrial", sans-serif; font-size: 25px; color: var(--ink); }
  .welcome-title .accent { font-size: 24px; }
  .welcome-text { left: 30px; top: 467px; width: 595px; font-size: 12.2px; line-height: 17.5px; color: var(--ink); }
  .welcome-text p { margin-bottom: 17.5px; }

  .advert { left: 31px; top: 724px; width: 591px; height: 133px; border-radius: 8px; background: linear-gradient(#6f7d90, #4e5b6c); box-shadow: 0 2px 5px rgba(0,0,0,.35); overflow: hidden; }
  .advert-art { left: 360px; top: 0; width: 231px; height: 133px; background: radial-gradient(ellipse at 50% 40%, #9aa5b3, #5a6779 75%); }
  .advert-title { left: 35px; top: 20px; font-family: "Questrial", sans-serif; font-size: 46px; color: #fff; }
  .advert-sub { left: 33px; top: 78px; font-family: "Questrial", sans-serif; font-size: 25px; color: #fff; }

  .finder { left: 672px; top: 447px; width: 270px; height: 409px; background: var(--peach); border: 1px solid var(--orange); border-radius: 8px; }
  .finder-flag { left: 646px; top: 478px; width: 42px; height: 41px; background: var(--peach); border: 1px solid var(--orange); border-right: none; border-radius: 8px 0 0 8px; }
  .finder-icon { left: 657px; top: 489px; width: 20px; height: 20px; border-radius: 50%; background: var(--orange); }
  .finder-card { left: 687px; top: 467px; width: 243px; height: 255px; background: var(--orange); }
  .finder-title { left: 0; top: 16px; width: 243px; text-align: center; font: 500 17px/21px "Ubuntu", sans-serif; color: #fff; }
  .finder-map { left: 30px; top: 70px; width: 183px; height: 170px; background: radial-gradient(circle, #fff 0 55%, var(--orange) 72%); opacity: .9; border-radius: 40%; }
  .keyword { left: 687px; top: 744px; width: 243px; height: 35px; background: #fff; border: 1px solid #ccc; border-radius: 3px; font-size: 12.5px; color: #333; display: flex; align-items: center; justify-content: center; }
  .btn-green { left: 687px; top: 793px; width: 243px; height: 36px; background: var(--green); border-radius: 3px; color: #fff; font: 500 17px "Ubuntu", sans-serif; display: flex; align-items: center; justify-content: center; }

  .featured-tab { left: 29px; top: 895px; width: 177px; height: 26px; background: var(--orange); color: #fff; font: 500 18px "Ubuntu", sans-serif; padding-left: 8px; display: flex; align-items: center; }
  .featured { left: 29px; top: 916px; width: 913px; height: 138px; background: var(--peach); border: 1px solid var(--orange); }
  .profile { top: 935px; width: 278px; height: 110px; background: linear-gradient(#fff, #ededed); border: 1px solid var(--orange); border-radius: 3px; }
  .profile-logo { left: 8px; top: 38px; width: 100px; font: 700 16px "Noto Sans", sans-serif; color: var(--ink); text-align: center; }
  .profile-title { left: 110px; top: 8px; font-family: "Questrial", sans-serif; font-size: 17.5px; color: var(--ink); }
  .profile-text { left: 110px; top: 34px; width: 165px; font-size: 12px; line-height: 14.5px; color: var(--ink); }
  .profile-more { left: 110px; top: 91px; font-size: 11px; font-weight: 700; letter-spacing: .5px; color: var(--ink); }

  .footer-line { left: 29px; top: 1105px; width: 913px; height: 1px; background: var(--line); }
  .footer-col { top: 1118px; font-family: Arial, sans-serif; font-size: 11.5px; line-height: 14.5px; color: #c0c5cb; }
  .footer-col strong { display: block; color: #6d7a88; font-size: 12px; margin-bottom: 6px; }
  .copyright { left: 785px; top: 1118px; font: 12px Arial, sans-serif; color: #6d7a88; }
</style>
</head>
<body>
  <header class="site-header abs"></header>
  <div class="brand abs"><span class="brand-dot"></span><span class="brand-name">TaskBloom</span></div>

  <nav>
    <div class="nav-tab home abs" style="left:338px;width:55px">
      <svg width="18" height="17" viewBox="0 0 18 17"><path d="M9 1 1 8h2.5v8h4v-5h3v5h4V8H17z" fill="#a8b3c1"/></svg>
    </div>
    <div class="nav-tab abs" style="left:402px;width:68px">FIND</div>
    <div class="nav-tab abs" style="left:480px;width:115px">ADVERTISE</div>
    <div class="nav-tab abs" style="left:605px;width:149px">HOW IT WORKS</div>
    <div class="nav-tab abs" style="left:764px;width:83px">BLOG</div>
    <div class="nav-tab abs" style="left:857px;width:84px">LOGIN</div>
  </nav>

  <div class="search abs">
    <div class="search-field">
      <svg width="14" height="14" viewBox="0 0 14 14"><circle cx="5.5" cy="5.5" r="4.2" fill="none" stroke="#8b99a9" stroke-width="1.8"/><path d="M8.6 8.6 13 13" stroke="#8b99a9" stroke-width="2"/></svg>
      Find a contractor
    </div>
    <div class="search-go">Go</div>
  </div>

  <section class="hero abs">
    <h1 class="hero-title abs">Changing how you <em>Find Job</em></h1>
    <p class="hero-text abs">Lorem Ipsum is simply dummy text of the printing and typesetting industry. Lorem Ipsum has been the industry's standard dummy text ever since the 1500s, when an unknown printer took a galley of type and scrambled it to make a type specimen book. It has survived not only five centuries, but also the leap into electronic typesetting, remaining essentially unchanged.</p>
    <div class="btn-orange abs">Read More</div>
    <span class="dot on abs" style="left:316px"></span>
    <span class="dot abs" style="left:336px"></span>
    <span class="dot abs" style="left:355px"></span>
    <div class="hero-art abs" role="img" aria-label="Illustration of an orange laptop showing a job search screen beside orange silhouettes of three professionals"></div>
  </section>

  <h2 class="welcome-title abs">Welcome to <span class="accent">TaskBloom</span></h2>
  <div class="welcome-text abs">
    <p>Lorem Ipsum is simply dummy text of the printing and typesetting industry. Lorem Ipsum has been the industry's standard dummy text ever since the 1500s, when an unknown printer took a galley of type and scrambled it to make a type specimen book. It has survived not only five centuries, but also the leap into electronic typesetting, remaining essentially unchanged.</p>
    <p>Lorem Ipsum is simply dummy text of the printing and typesetting industry. Lorem Ipsum has been the industry's standard dummy text ever since the 1500s, when an unknown printer took a galley of type and scrambled it to make a type specimen book. It has survived not only five centuries, but also the leap into electronic typesetting, remaining essentially unchanged.</p>
    <p>Lorem Ipsum is simply dummy text of the printing and typesetting industry. Lorem Ipsum has been the industry's standard dummy text ever since the 1500s, when an unknown printer took a galley of type and scrambled it to make a type specimen book.</p>
  </div>

  <section class="advert abs">
    <div class="advert-art abs" role="img" aria-label="3D illustration of large JOBS letters with a crowd of small grey figures"></div>
    <div class="advert-title abs">ADVERTISE</div>
    <div class="advert-sub abs">Life In The Search Lane</div>
  </section>

  <aside>
    <div class="finder abs"></div>
    <div class="finder-flag abs"></div>
    <div class="finder-icon abs">
      <svg width="20" height="20" viewBox="0 0 20 20"><g fill="none" stroke="#fff" stroke-width="1.3"><circle cx="10" cy="10" r="6"/><ellipse cx="10" cy="10" rx="2.6" ry="6"/><path d="M4 10h12"/></g></svg>
    </div>
    <div class="finder-card abs">
      <div class="finder-title abs">Find Highly Skilled<br>Professionals:</div>
      <div class="finder-map abs" role="img" aria-label="White map of Australia divided into states"></div>
    </div>
    <div class="keyword abs">Keyword...</div>
    <div class="btn-green abs">FIND CONTRACTORS</div>
  </aside>

  <div class="featured abs"></div>
  <div class="featured-tab abs">Featured Profiles:</div>

  <article class="profile abs" style="left:40px">
    <div class="profile-logo abs" role="img" aria-label="Company logo">&nbsp;</div>
    <div class="profile-title abs">Company Name:</div>
    <p class="profile-text abs">Lorem Ipsum is simply dummy text of the printing and typesetting industry.</p>
    <div class="profile-more abs">Read More</div>
  </article>
  <article class="profile abs" style="left:346px">
    <div class="profile-logo abs">Arvelo</div>
    <div class="profile-title abs">Company Name:</div>
    <p class="profile-text abs">Lorem Ipsum is simply dummy text of the printing and typesetting industry.</p>
    <div class="profile-more abs">Read More</div>
  </article>
  <article class="profile abs" style="left:652px">
    <div class="profile-logo abs">Nexor</div>
    <div class="profile-title abs">Company Name:</div>
    <p class="profile-text abs">Lorem Ipsum is simply dummy text of the printing and typesetting industry.</p>
    <div class="profile-more abs">Read More</div>
  </article>

  <footer>
    <div class="footer-line abs"></div>
    <div class="footer-col abs" style="left:32px"><strong>About Us</strong>Features<br>Pricing<br>Team</div>
    <div class="footer-col abs" style="left:110px"><strong>Browse</strong>By State<br>By Business<br>Search</div>
    <div class="footer-col abs" style="left:192px"><strong>Sign up</strong></div>
    <div class="copyright abs">© Copyright 2010 TaskBloom</div>
  </footer>
</body>
</html>
```